Veltrane Partners Inc. - Cyber security company needs web site redesign

Need to redesign the corporate web page. Static content with no rss feeds. Web page is for basic marketing and corporate information. VPI is a management and cyber security consulting firm. The company logo has been redesigned and would like to incorporate this new logo into the design. Also need to reference MADE IN USA logo, SDVOSB logo, Include the current content from the existing web page and will revise as needed
Updates

Target Market(s)

Government and Commercial Clients and potential new employees

Industry/Entity Type

It Company

Number of Pages Required

1 page

Font styles to use
Sans Serif

Requirements
Must have
• New Veltrane Partners Logo
• MADE IN USA logo
• SDVOSB logo
• Cyber security theme
Nice to have
• animation
• Cyber security related graphics
Should not have
• Search and News sections

```html
<!DOCTYPE html>
<html lang="en">
<head>
<meta charset="utf-8">
<title>Veltrane Partners Inc.</title>
<link href="https://fonts.googleapis.com/css2?family=Raleway:wght@400;500;600&family=Open+Sans:wght@400;600;700&display=swap" rel="stylesheet">
<style>
:root{
  --gold:#c9a22c;
  --gold-dark:#a9851c;
  --black:#050505;
  --nav:#0d0d0d;
  --ink:#222;
  --muted:#555;
  --light:#f0f0f0;
  --white:#fff;
  --line:#3a3a3a;
}
*{box-sizing:border-box;margin:0;padding:0}
html,body{width:1200px;height:3226px;overflow:hidden}
body{position:relative;background:var(--white);font-family:"Open Sans",Arial,sans-serif;color:var(--ink)}
.abs{position:absolute}

/* header */
.topbar{left:0;top:0;width:1200px;height:105px;background:var(--white)}
.contact-item{top:28px;display:flex;align-items:center;gap:14px;font-size:15px;line-height:19px}
.contact-item small{display:block;font-size:15px;color:var(--muted)}
.contact-item b{font-weight:700;color:var(--ink)}
.navbar{left:0;top:105px;width:1200px;height:50px;background:var(--nav)}
.nav{left:313px;top:105px;height:50px;display:flex}
.nav a{width:158px;height:50px;line-height:50px;text-align:center;color:var(--white);font-size:16px;font-weight:600;text-decoration:none;border-right:1px solid var(--line);text-transform:uppercase}
.nav a:last-child{border-right:none}
.nav a.active{color:var(--gold)}
.brand{left:135px;top:0;width:152px;height:215px;background:var(--white);border:3px solid var(--gold);border-top:none;z-index:3;display:flex;flex-direction:column;align-items:center;justify-content:center;gap:14px;text-align:center}
.brand-mark{width:46px;height:46px;background:var(--gold)}
.brand-name{font-family:"Open Sans",Arial,sans-serif;font-weight:700;font-size:15px;line-height:20px;color:var(--gold)}

/* hero */
.hero{left:0;top:155px;width:1200px;height:515px;background:linear-gradient(100deg,#5d6d7c 0%,#8fa6b8 25%,#3b4754 45%,#7b1e22 52%,#3a4350 62%,#9fbcd2 85%,#c9dbe8 100%)}
.hero-caption{left:0;top:580px;width:1200px;height:90px;background:rgba(0,0,0,.55);color:var(--white);font-family:"Raleway",Arial,sans-serif;font-weight:500;font-size:36px;line-height:90px;text-align:center;padding-right:18px}
.hero-arrow{top:390px;width:46px;height:40px;background:rgba(40,40,40,.85)}

/* welcome */
.welcome{left:0;top:670px;width:1200px;height:390px;background:linear-gradient(135deg,#f6f6f6,#e4e4e4)}
.welcome-title{left:131px;top:711px;font-family:"Raleway",Arial,sans-serif;font-weight:500;font-size:34px;color:var(--black);letter-spacing:.5px}
.welcome-text{left:131px;top:757px;width:580px;font-size:14px;line-height:21.5px;color:#333}
.feature{top:896px;display:flex;gap:16px}
.feature h3{font-size:17px;font-weight:700;color:var(--black);margin-bottom:4px}
.feature p{font-size:14px;line-height:19px;color:#444;width:210px}
.divider{left:420px;top:896px;width:1px;height:95px;background:#c9c9c9}

.inquiry{left:757px;top:712px;width:310px;height:300px;background:var(--white);border:1px solid #ddd}
.inquiry-tab{left:798px;top:706px;width:230px;height:48px;background:var(--gold);color:var(--white);font-size:22px;text-align:center;line-height:46px;border-radius:0 0 4px 4px}
.field{left:776px;width:274px;height:37px;border:1px solid #d9d9d9;background:var(--white);font-size:12px;color:#999;padding-left:12px;line-height:35px}
.submit{left:776px;top:955px;width:134px;height:36px;background:var(--black);color:var(--white);font-weight:700;font-size:14px;line-height:36px;text-align:center;text-transform:uppercase}

/* services */
.services{left:0;top:1060px;width:1200px;height:1202px;background:var(--black)}
.services-title{left:576px;top:1118px;width:396px;text-align:center;font-family:"Raleway",Arial,sans-serif;font-size:34px;color:var(--white);letter-spacing:1px}
.service{left:576px;width:491px;height:131px;border-bottom:1px solid #2c2c2c;display:flex;align-items:center;gap:36px;padding-left:6px}
.service:last-child{border:none}
.service .icon{width:95px;height:95px;border-radius:50%;background:var(--white);display:flex;align-items:center;justify-content:center;flex:none}
.service h3{font-family:"Raleway",Arial,sans-serif;font-weight:500;font-size:26px;color:var(--white);margin-bottom:6px}
.service p{font-size:12.5px;line-height:19px;color:#ddd;width:340px}
.service.featured{background:linear-gradient(var(--gold),var(--gold-dark));border-radius:70px 0 0 70px;border:none;left:566px;width:501px;padding-left:16px}
.service.featured .icon{background:var(--black);box-shadow:0 0 0 4px rgba(0,0,0,.25)}
.service.featured h3,.service.featured p{color:var(--black)}

/* cards */
.card{width:290px;text-align:center}
.card h3{font-family:"Raleway",Arial,sans-serif;font-weight:500;font-size:23px;line-height:27px;color:var(--black);margin-top:20px}
.card p{font-size:13px;line-height:20px;color:#555;margin:14px 14px 0}
.btn{display:inline-block;margin-top:18px;width:132px;height:38px;border:2px solid #333;font-size:14px;line-height:34px;color:#333}
.btn.gold{background:var(--gold);border-color:var(--gold);color:var(--white)}

/* footer */
.footer{left:0;top:2788px;width:1200px;height:390px;background:var(--black);color:var(--white)}
.footer h4{font-family:"Raleway",Arial,sans-serif;font-weight:500;font-size:24px;color:var(--white)}
.quick-links{left:131px;top:2878px}
.quick-links ul{list-style:none;margin-top:20px}
.quick-links li{font-size:15px;line-height:34px}
.map{left:344px;top:2842px;width:280px;height:280px;border-radius:50%;border:5px solid #d8c58a;background:radial-gradient(circle at 55% 45%,#e9eef2 0%,#cfdbe3 45%,#a9c3d4 100%)}
.contact{left:660px;top:2878px}
.contact ul{list-style:none;margin-top:18px}
.contact li{display:flex;gap:14px;font-size:15px;line-height:22px;margin-bottom:12px;align-items:flex-start}
.badge{width:94px;height:94px;border-radius:50%;background:#d9d9d9;border:4px solid #888}
.copyright{left:0;top:3178px;width:1200px;height:48px;background:var(--gold);color:var(--white);font-size:14px;line-height:48px;text-align:center}
</style>
</head>
<body>

<header>
  <div class="abs topbar"></div>
  <div class="abs brand">
    <span class="brand-mark"></span>
    <span class="brand-name">Veltrane<br>Partners Inc.</span>
  </div>
  <div class="abs contact-item" style="left:672px">
    <svg width="34" height="34" viewBox="0 0 24 24"><path fill="#222" d="M6.6 10.8a15 15 0 0 0 6.6 6.6l2.2-2.2c.3-.3.7-.4 1-.2 1.1.4 2.3.6 3.6.6.6 0 1 .4 1 1V20c0 .6-.4 1-1 1C10.6 21 3 13.4 3 4c0-.6.4-1 1-1h3.5c.6 0 1 .4 1 1 0 1.3.2 2.5.6 3.6.1.3 0 .7-.2 1z"/></svg>
    <div><small>Call Us:</small><b>012.345.6789</b></div>
  </div>
  <div class="abs contact-item" style="left:875px">
    <svg width="40" height="30" viewBox="0 0 40 30"><rect x="2" y="3" width="36" height="24" fill="none" stroke="#222" stroke-width="2.5"/><path d="M2 3l18 14 18-14" fill="none" stroke="#222" stroke-width="2.5"/></svg>
    <div><small>Mail Us:</small><b>info@vpi-partners.com</b></div>
  </div>
  <div class="abs navbar"></div>
  <nav class="abs nav">
    <a class="active">Home</a><a>Services</a><a>About Us</a><a>Careers</a><a>Contact Us</a>
  </nav>
</header>

<section>
  <div class="abs hero" role="img" aria-label="Cracked digital security shields over a field of hexadecimal code, one shield glowing red"></div>
  <div class="abs hero-arrow" style="left:0"><svg width="46" height="40"><path d="M27 12l-8 8 8 8" fill="none" stroke="#fff" stroke-width="3"/></svg></div>
  <div class="abs hero-arrow" style="left:1154px"><svg width="46" height="40"><path d="M19 12l8 8-8 8" fill="none" stroke="#fff" stroke-width="3"/></svg></div>
  <div class="abs hero-caption">We Are A Management And Cyber Security Consulting Firm</div>
</section>

<section>
  <div class="abs welcome"></div>
  <h1 class="abs welcome-title">WELCOME TO VELTRANE PARTNERS</h1>
  <p class="abs welcome-text">Lorem ipsum dolor sit amet, ex vim quem primis. Quot suavitate molestiae ex usu. Ridens eleifend ei sea, aeterno feugait molestie at eum, mel vitae principes sententiae an. Ex adolescens scripserit eam, per nisl laboramus ea. Cu est opulo senserit, te quem nonumy percipit cum. Invidunt molestiae qui in. Corpora iudicabit ius eu. Regione ceteros efficiantur ut quo. Semper labores accusam in eam.</p>
  <div class="abs feature" style="left:136px">
    <svg width="44" height="40" viewBox="0 0 44 40"><circle cx="22" cy="10" r="7" fill="#222"/><circle cx="9" cy="16" r="5" fill="var(--gold)"/><circle cx="35" cy="16" r="5" fill="var(--gold)"/><path d="M10 38c0-9 5-16 12-16s12 7 12 16z" fill="#222"/><path d="M0 36c0-7 4-12 9-12s7 3 7 6v6zM44 36c0-7-4-12-9-12s-7 3-7 6v6z" fill="var(--gold)"/></svg>
    <div><h3>Who We Are</h3><p>Sed ut perspiciatis unde omnisl istei wisit voluptatem accusank tium.</p></div>
  </div>
  <div class="abs divider"></div>
  <div class="abs feature" style="left:455px">
    <svg width="42" height="42" viewBox="0 0 42 42"><circle cx="21" cy="21" r="18" fill="none" stroke="#222" stroke-width="4"/><circle cx="21" cy="21" r="10" fill="none" stroke="var(--gold)" stroke-width="4"/><circle cx="21" cy="21" r="3" fill="#222"/><path d="M21 21L38 4" stroke="#222" stroke-width="3"/></svg>
    <div><h3>Our Vision</h3><p>Sed ut perspiciatis unde omnisl istei wisit voluptatem accusank tium.</p></div>
  </div>

  <div class="abs inquiry"></div>
  <div class="abs inquiry-tab">Quick Inquiry</div>
  <div class="abs field" style="top:770px">First Name</div>
  <div class="abs field" style="top:815px">Last Name</div>
  <div class="abs field" style="top:860px">Email Id</div>
  <div class="abs field" style="top:907px">Inquiry Type
    <svg class="abs" style="right:14px;top:15px" width="12" height="8"><path d="M0 0h12L6 7z" fill="#666"/></svg>
  </div>
  <div class="abs submit">Submit</div>
</section>

<section>
  <div class="abs services"></div>
  <h2 class="abs services-title">OUR SERVICES</h2>
  <div class="abs service" style="top:1172px"><span class="icon"><svg width="46" height="46" viewBox="0 0 46 46"><circle cx="23" cy="23" r="20" fill="#111"/><circle cx="23" cy="23" r="13" fill="none" stroke="#fff" stroke-width="3"/><path d="M12 34L34 12" stroke="#fff" stroke-width="3"/></svg></span><div><h3>Threat Analysis</h3><p>Lorem ipsum dolor sit ameter consectetuer adip iscing elit, diam nonummy</p></div></div>
  <div class="abs service" style="top:1303px"><span class="icon"><svg width="44" height="48" viewBox="0 0 44 48"><path d="M22 2l19 7v13c0 12-8 20-19 24C11 42 3 34 3 22V9z" fill="#111"/><path d="M13 24l7 7 12-13" fill="none" stroke="#fff" stroke-width="4"/></svg></span><div><h3>Threat Mitigation</h3><p>Lorem ipsum dolor sit ameter consectetuer adip iscing elit, diam nonummy</p></div></div>
  <div class="abs service" style="top:1434px"><span class="icon"><svg width="46" height="46" viewBox="0 0 46 46"><circle cx="23" cy="23" r="20" fill="#111"/><path d="M6 16c10 4 24 4 34 0M4 28c12 5 26 5 38 0M18 4c-6 12-6 26 0 38" fill="none" stroke="#fff" stroke-width="3"/></svg></span><div><h3>Automated Solutions</h3><p>Lorem ipsum dolor sit ameter consectetuer adip iscing elit, diam nonummy</p></div></div>
  <div class="abs service" style="top:1565px"><span class="icon"><svg width="48" height="46" viewBox="0 0 48 46"><ellipse cx="24" cy="26" rx="10" ry="13" fill="#111"/><circle cx="24" cy="11" r="6" fill="#111"/><path d="M4 16l12 6M44 16l-12 6M2 28h12M46 28H34M6 42l10-8M42 42l-10-8" stroke="#111" stroke-width="3"/></svg></span><div><h3>Malware Analysis</h3><p>Lorem ipsum dolor sit ameter consectetuer adip iscing elit, diam nonummy</p></div></div>
  <div class="abs service" style="top:1696px"><span class="icon"><svg width="44" height="48" viewBox="0 0 44 48"><path d="M22 2l19 7v13c0 12-8 20-19 24C11 42 3 34 3 22V9z" fill="#111"/><path d="M22 8v34M8 22h28" stroke="#fff" stroke-width="3"/></svg></span><div><h3>Security Services</h3><p>Lorem ipsum dolor sit ameter consectetuer adip iscing elit, diam nonummy</p></div></div>
  <div class="abs service featured" style="top:1827px"><span class="icon"><svg width="48" height="46" viewBox="0 0 48 46"><circle cx="24" cy="10" r="6" fill="#fff"/><circle cx="8" cy="34" r="5" fill="#fff"/><circle cx="40" cy="34" r="5" fill="#fff"/><circle cx="24" cy="38" r="5" fill="#fff"/><path d="M24 16v17M20 15L10 30M28 15l10 15" stroke="#fff" stroke-width="3"/></svg></span><div><h3>Management Consulting</h3><p>Lorem ipsum dolor sit ameter consectetuer adip iscing elit, diam nonummy</p></div></div>
  <div class="abs service" style="top:1958px"><span class="icon"><svg width="44" height="48" viewBox="0 0 44 48"><circle cx="16" cy="8" r="6" fill="#111"/><path d="M6 18h20v14H22v14H10V32H6z" fill="#111"/><path d="M28 16l13 4v9c0 8-6 13-13 16-7-3-13-8-13-16" fill="#111" stroke="#fff" stroke-width="2"/></svg></span><div><h3>Cyber Threat Intelligence</h3><p>Lorem ipsum dolor sit ameter consectetuer adip iscing elit, diam nonummy</p></div></div>
  <div class="abs service" style="top:2089px"><span class="icon"><svg width="48" height="48" viewBox="0 0 48 48"><path d="M6 42L26 22M10 6a8 8 0 0 0 10 10L40 38l-4 4-20-20A8 8 0 0 1 6 10z" stroke="#111" stroke-width="5" fill="none"/><ellipse cx="36" cy="14" rx="6" ry="8" fill="#111"/><path d="M28 8l-4-3M44 8l4-3M28 16h-4M44 16h4" stroke="#111" stroke-width="2"/></svg></span><div><h3>Threat Operations</h3><p>Lorem ipsum dolor sit ameter consectetuer adip iscing elit, diam nonummy</p></div></div>
</section>

<section>
  <div class="abs card" style="left:130px;top:2300px">
    <svg width="290" height="200" viewBox="0 0 290 200" role="img" aria-label="Hand touching a glowing network of connected people icons"><defs><linearGradient id="g1" x1="0" y1="0" x2="1" y2="1"><stop offset="0" stop-color="#0d2a52"/><stop offset="1" stop-color="#3b7fc4"/></linearGradient></defs><polygon points="10,10 280,10 280,170 145,195 10,170" fill="url(#g1)"/><polygon points="3,3 287,3 287,175 145,198 3,175" fill="none" stroke="#999" stroke-width="2" stroke-dasharray="5 4"/></svg>
    <h3>Careers at<br>Veltrane Partners</h3>
    <p>Lorem ipsum dolor sit amet, consectetuer in the adipiscing elit, sed diam nonummy niblers and euismod tincidunt ut laoreet dolore magnagt...</p>
    <span class="btn">Read More</span>
  </div>
  <div class="abs card" style="left:455px;top:2300px">
    <svg width="290" height="200" viewBox="0 0 290 200" role="img" aria-label="Server room corridor glowing in blue light"><defs><linearGradient id="g2" x1="0" y1="0" x2="0" y2="1"><stop offset="0" stop-color="#0a1430"/><stop offset=".5" stop-color="#2f6fd0"/><stop offset="1" stop-color="#0a1430"/></linearGradient></defs><polygon points="10,10 280,10 280,170 145,195 10,170" fill="url(#g2)"/><polygon points="3,3 287,3 287,175 145,198 3,175" fill="none" stroke="#999" stroke-width="2" stroke-dasharray="5 4"/></svg>
    <h3>About<br>Veltrane Partners</h3>
    <p>Lorem ipsum dolor sit amet, consectetuer in the adipiscing elit, sed diam nonummy niblers and euismod tincidunt ut laoreet dolore magnagt...</p>
    <span class="btn gold">Read More</span>
  </div>
  <div class="abs card" style="left:780px;top:2300px">
    <svg width="290" height="200" viewBox="0 0 290 200" role="img" aria-label="Hand sketching a staircase with a climbing figure on a grey wall"><defs><linearGradient id="g3" x1="0" y1="0" x2="1" y2="1"><stop offset="0" stop-color="#9a948c"/><stop offset="1" stop-color="#5f5a55"/></linearGradient></defs><polygon points="10,10 280,10 280,170 145,195 10,170" fill="url(#g3)"/><polygon points="3,3 287,3 287,175 145,198 3,175" fill="none" stroke="#999" stroke-width="2" stroke-dasharray="5 4"/></svg>
    <h3>Why<br>Veltrane Partners?</h3>
    <p>Lorem ipsum dolor sit amet, consectetuer in the adipiscing elit, sed diam nonummy niblers and euismod tincidunt ut laoreet dolore magnagt...</p>
    <span class="btn">Read More</span>
  </div>
</section>

<footer>
  <div class="abs footer"></div>
  <div class="abs quick-links">
    <h4>Quick Links</h4>
    <ul><li>&gt; Home</li><li>&gt; Services</li><li>&gt; About Us</li><li>&gt; Careers</li><li>&gt; Contact Us</li></ul>
  </div>
  <div class="abs map" role="img" aria-label="Street map of the office location with a location pin"></div>
  <div class="abs contact">
    <h4>Contact Details</h4>
    <ul>
      <li><svg width="16" height="22" viewBox="0 0 16 22"><path d="M8 0a8 8 0 0 0-8 8c0 6 8 14 8 14s8-8 8-14a8 8 0 0 0-8-8z" fill="#fff"/><circle cx="8" cy="8" r="3" fill="#000"/></svg><span>Lorem ipsum dolor sit amet,<br>ex vim quem primis - 12345</span></li>
      <li><svg width="16" height="16" viewBox="0 0 24 24"><path fill="#fff" d="M6.6 10.8a15 15 0 0 0 6.6 6.6l2.2-2.2c.3-.3.7-.4 1-.2 1.1.4 2.3.6 3.6.6.6 0 1 .4 1 1V20c0 .6-.4 1-1 1C10.6 21 3 13.4 3 4c0-.6.4-1 1-1h3.5c.6 0 1 .4 1 1 0 1.3.2 2.5.6 3.6.1.3 0 .7-.2 1z"/></svg><span>012.345.6789</span></li>
      <li><svg width="16" height="16" viewBox="0 0 24 24"><path fill="#fff" d="M6.6 10.8a15 15 0 0 0 6.6 6.6l2.2-2.2c.3-.3.7-.4 1-.2 1.1.4 2.3.6 3.6.6.6 0 1 .4 1 1V20c0 .6-.4 1-1 1C10.6 21 3 13.4 3 4c0-.6.4-1 1-1h3.5c.6 0 1 .4 1 1 0 1.3.2 2.5.6 3.6.1.3 0 .7-.2 1z"/></svg><span>012.345.6789</span></li>
      <li><svg width="16" height="14" viewBox="0 0 16 12"><rect x="0" y="0" width="16" height="12" fill="#fff"/><path d="M0 0l8 6 8-6" fill="none" stroke="#000" stroke-width="1.5"/></svg><span>info@vpi-partners.com</span></li>
    </ul>
  </div>
  <div class="abs badge" style="left:921px;top:2871px"></div>
  <div class="abs badge" style="left:921px;top:2995px"></div>
  <div class="abs copyright">Copyright 2016 - VELTRANE PARTNERS | All Rights Reserved</div>
</footer>

</body>
</html>
```